Coral Marriage Counsel Partners Billboard

We are looking for a billboard design for a Florida divorce law firm. We are unique in the legal field for offering flat fee pricing. Other law firms are expensive, charging hourly rates. We have A LOT of lawyers advertising for personal injury, so we are looking for something fun that will catch the attention and drive home the message that we are an affordable firm to hire for their divorce because we charge a fixed fee. We want people to be directed to steadyratesplit.example

Target Market(s)

Individual seeking a fast and affordable divorce at a fixed fee instead of hourly

Industry/Entity Type

Legal

Requirements
Must have
• Name of firm, logo, steadyratesplit.example, and in small font: Main Office Harbor Point
Should not have
• Promises. Price

```html
<!DOCTYPE html>
<html lang="en">
<head>
<meta charset="utf-8">
<title>Coral Marriage Counsel Partners Billboard</title>
<link rel="stylesheet" href="https://fonts.googleapis.com/css2?family=Montserrat:wght@400;500;600;700;800&display=swap">
<style>
  :root {
    --gold: #a8821f;
    --navy: #1e4571;
    --ink: #1f1f1f;
    --paper: #ffffff;
    --backdrop: #e9e8e6;
    --haze: #f1f1f2;
  }
  * { margin: 0; padding: 0; box-sizing: border-box; }
  html, body { width: 1121px; height: 1200px; overflow: hidden; }
  body {
    background: var(--backdrop);
    font-family: "Montserrat", sans-serif;
    color: var(--ink);
    position: relative;
  }
  .billboard {
    position: absolute;
    left: 40px; top: 427px;
    width: 1040px; height: 346px;
    background: linear-gradient(90deg, var(--haze) 0%, var(--paper) 45%, var(--paper) 100%);
    box-shadow: 10px 12px 18px rgba(0,0,0,0.28);
    overflow: hidden;
  }
  .headline-band {
    position: absolute; left: 0; top: 0;
    width: 100%; height: 73px;
    background: var(--gold);
    display: flex; align-items: center; justify-content: center;
  }
  .headline {
    color: #fff; font-weight: 800; font-size: 42px; letter-spacing: 0.2px;
  }
  .brand {
    position: absolute; left: 40px; top: 92px; width: 290px;
    display: flex; flex-direction: column; align-items: center;
  }
  .brand-mark {
    width: 58px; height: 58px; border-radius: 50%;
    background: var(--navy);
  }
  .brand-name {
    margin-top: 10px; text-align: center;
    font-weight: 700; font-size: 19px; line-height: 1.15;
    color: var(--navy); text-transform: uppercase; letter-spacing: 0.6px;
  }
  .contact {
    position: absolute; left: 40px; width: 290px; text-align: center;
  }
  .web { top: 249px; font-size: 14px; color: var(--ink); }
  .web b { color: var(--navy); font-weight: 600; }
  .call { top: 270px; font-size: 20px; font-weight: 700; color: var(--navy); }
  .call span { color: var(--gold); }
  .office-pill {
    position: absolute; left: 73px; top: 300px;
    width: 184px; height: 24px;
    border: 1.5px solid var(--ink); border-radius: 12px;
    display: flex; align-items: center; justify-content: center; gap: 5px;
  }
  .office-pill small { font-size: 10px; color: var(--gold); font-weight: 500; }
  .office-pill strong { font-size: 14px; color: var(--navy); font-weight: 700; }
  .portrait {
    position: absolute; left: 378px; top: 78px;
    width: 226px; height: 268px;
    background: linear-gradient(180deg, #cfcfd2 0%, #2b2d34 45%, #1b1d24 100%);
    border-radius: 90px 90px 10px 10px;
  }
  .nameplate {
    position: absolute; left: 366px; top: 307px;
    width: 224px; height: 39px;
    background: var(--gold);
    clip-path: polygon(8% 0, 92% 0, 100% 100%, 0 100%);
    color: #fff; text-align: center;
    display: flex; flex-direction: column; justify-content: center;
  }
  .nameplate strong { font-size: 14px; font-weight: 700; line-height: 1.1; }
  .nameplate span { font-size: 12px; font-weight: 400; }
  .pitch { position: absolute; left: 625px; top: 88px; width: 410px; }
  .pitch h2 { font-size: 17px; font-weight: 700; color: var(--gold); line-height: 22px; }
  .pitch p { font-size: 16.5px; line-height: 22px; font-weight: 500; white-space: nowrap; }
  .features {
    position: absolute; left: 625px; top: 207px;
    width: 415px; height: 75px;
    background: var(--navy);
    display: flex;
  }
  .feature {
    flex: 1; position: relative;
    display: flex; align-items: flex-end; justify-content: center;
    padding-bottom: 14px;
    color: #fff; font-size: 11.5px; font-weight: 700; text-align: center; line-height: 1.35;
  }
  .feature + .feature::before {
    content: ""; position: absolute; left: 0; top: 20px; bottom: 10px;
    width: 1px; background: rgba(255,255,255,0.7);
  }
  .feature-icon {
    position: absolute; left: 50%; top: -24px; transform: translateX(-50%);
    width: 40px; height: 40px;
  }
  .badges {
    position: absolute; left: 640px; top: 293px; width: 390px; height: 42px;
    display: flex; justify-content: space-between; align-items: center;
  }
  .badge { background: var(--navy); }
  .badge.tall { width: 28px; height: 40px; background: #1c1c1c; }
  .badge.strip { width: 56px; height: 14px; background: #c7322f; }
  .badge.shield { width: 40px; height: 38px; background: var(--navy); clip-path: polygon(0 0,100% 0,100% 70%,50% 100%,0 70%); }
  .badge.tag { width: 52px; height: 22px; background: #2c5e9a; border-radius: 3px; }
  .badge.seal { width: 38px; height: 38px; border-radius: 50%; background: #d6c27a; }
  .badge.seal.blue { background: #3e4f9a; }
</style>
</head>
<body>
  <main class="billboard">
    <header class="headline-band">
      <h1 class="headline">Are You In Need Of A Divorce Attorney?</h1>
    </header>

    <section class="brand">
      <div class="brand-mark" aria-hidden="true"></div>
      <div class="brand-name">Coral Marriage<br>Counsel Partners</div>
    </section>

    <p class="contact web">www.<b>steadyratesplit</b>.example</p>
    <p class="contact call"><span>Call</span> 855-010-4477</p>
    <div class="office-pill"><small>Main Office</small><strong>Harbor Point</strong></div>

    <div class="portrait" role="img" aria-label="Photo of the attorney in a dark suit and gold tie"></div>
    <div class="nameplate"><strong>Mateo R. Delgado</strong><span>Divorce Attorneys</span></div>

    <section class="pitch">
      <h2>Serving all of Florida</h2>
      <p>Dedicated to protecting your rights. We can<br>help you gain the freedom and peace of mind<br>you deserve.</p>
    </section>

    <section class="features">
      <div class="feature">
        <svg class="feature-icon" viewBox="0 0 40 40" aria-hidden="true">
          <circle cx="20" cy="20" r="19" fill="#fff"/><circle cx="20" cy="20" r="16" fill="#a8821f"/>
          <circle cx="20" cy="20" r="9" fill="none" stroke="#fff" stroke-width="2"/>
          <path d="M20 14v6l4 3" fill="none" stroke="#fff" stroke-width="2" stroke-linecap="round"/>
        </svg>
        24/7<br>Availability
      </div>
      <div class="feature">
        <svg class="feature-icon" viewBox="0 0 40 40" aria-hidden="true">
          <circle cx="20" cy="20" r="19" fill="#fff"/><circle cx="20" cy="20" r="16" fill="#a8821f"/>
          <path d="M20 11v17M14 28h12M12 15h16M12 15l-3 7h6zM28 15l-3 7h6z" fill="none" stroke="#fff" stroke-width="1.6" stroke-linejoin="round"/>
        </svg>
        Flat Fee<br>for most cases
      </div>
      <div class="feature">
        <svg class="feature-icon" viewBox="0 0 40 40" aria-hidden="true">
          <circle cx="20" cy="20" r="19" fill="#fff"/><circle cx="20" cy="20" r="16" fill="#a8821f"/>
          <path d="M13 20l5 5 9-10" fill="none" stroke="#fff" stroke-width="2.4" stroke-linecap="round" stroke-linejoin="round"/>
        </svg>
        100%<br>Dedicated
      </div>
      <div class="feature">
        <svg class="feature-icon" viewBox="0 0 40 40" aria-hidden="true">
          <circle cx="20" cy="20" r="19" fill="#fff"/><circle cx="20" cy="20" r="16" fill="#a8821f"/>
          <rect x="12" y="13" width="16" height="15" rx="1.5" fill="none" stroke="#fff" stroke-width="1.8"/>
          <path d="M12 17h16M16 11v4M24 11v4M15 21h2M19 21h2M23 21h2M15 24h2M19 24h2" stroke="#fff" stroke-width="1.6"/>
        </svg>
        20 Years<br>in Practice
      </div>
    </section>

    <section class="badges" aria-label="Recognition badges">
      <div class="badge tall"></div>
      <div class="badge strip"></div>
      <div class="badge shield"></div>
      <div class="badge tag"></div>
      <div class="badge seal"></div>
      <div class="badge seal blue"></div>
    </section>
  </main>
</body>
</html>
```